Website redesign

Looking to redesign our existing website. (hire4ward.com.au)
New design needs to be bright, fun and have an easy flowing.
The website needs to be design with call to action.

Some examples of other websites:
brightdesk.com
lendnest.com.au

We are happy with the content of our existing website.

Target Market(s)

other businesses

Industry/Entity Type

Business Service

Number of Pages Required

5+ page

Requirements
Must have
• Theme redesign
Cool animation similar to brightdesk.com

```html
<!DOCTYPE html>
<html lang="en">
<head>
<meta charset="utf-8">
<title>Hire4ward — Virtual Assistant</title>
<link rel="stylesheet" href="https://fonts.googleapis.com/css2?family=Montserrat:wght@400;500;600;700&family=Roboto:wght@400;500&display=swap">
<style>
  :root {
    --ink: #2b2b2b;
    --white: #ffffff;
    --blue-deep: #0b4fa8;
    --blue: #1470c4;
    --teal: #1bb3b0;
    --sky: #3fc3f0;
    --grey-bg: #ebebeb;
    --grey-text: #555555;
    --icon-dark: #3a3a3a;
    --icon-grey: #9a9a9a;
  }
  * { box-sizing: border-box; margin: 0; padding: 0; }
  html, body { width: 1200px; height: 720px; overflow: hidden; background: var(--white); }
  body { font-family: "Montserrat", sans-serif; color: var(--ink); }

  .page { position: relative; width: 1200px; height: 720px; overflow: hidden; }

  /* Top contact bar */
  .topbar { height: 46px; display: flex; align-items: stretch; background: var(--white); }
  .topbar__info { flex: 1; display: flex; justify-content: center; align-items: center; gap: 56px;
    font-family: "Roboto", sans-serif; font-size: 13px; letter-spacing: 1.6px; color: var(--ink); padding-left: 120px; }
  .topbar__social { display: flex; align-items: center; width: 250px; }
  .social-dot { width: 14px; height: 14px; border-radius: 3px; background: var(--icon-grey); margin-left: 20px; }
  .social-dot--first { width: 36px; height: 46px; border-radius: 0; background: var(--icon-dark); margin-left: 0; }

  /* Hero */
  .hero { position: relative; height: 430px;
    background: linear-gradient(115deg, var(--blue-deep) 0%, var(--blue) 45%, var(--teal) 100%); overflow: hidden; }
  .hero__photo { position: absolute; right: 0; top: 0; width: 330px; height: 430px;
    background: linear-gradient(180deg, rgba(255,255,255,0.10), rgba(20,40,70,0.55)); }
  .hero__inner { position: absolute; left: 0; right: 330px; top: 0; bottom: 0; text-align: center; color: var(--white); }
  .brand { margin-top: 30px; display: inline-flex; align-items: center; gap: 8px; font-size: 24px; font-weight: 600; color: var(--white); }
  .brand__mark { width: 16px; height: 16px; border-radius: 50%; background: var(--sky); }
  .nav { margin-top: 28px; display: flex; justify-content: center; gap: 20px; font-size: 13px; font-weight: 500; letter-spacing: 0.3px; }
  .nav__item--active { background: var(--teal); padding: 2px 7px; font-weight: 700; }
  .headline { margin-top: 78px; font-size: 36px; font-weight: 600; letter-spacing: 0.5px; line-height: 1; }
  .headline__accent { color: var(--sky); }
  .subhead { margin-top: 10px; font-size: 22px; font-weight: 600; }
  .tagline { margin-top: 22px; font-size: 16px; line-height: 1.35; font-weight: 400; }
  .cta { margin-top: 20px; display: inline-flex; align-items: center; font-size: 20px; font-weight: 500; }
  .cta__label { background: var(--white); color: var(--ink); padding: 4px 12px; border-radius: 14px 0 0 14px; }
  .cta__number { background: var(--teal); color: var(--white); padding: 4px 14px; border-radius: 0 14px 14px 0; }

  /* Outsourcing section */
  .outsourcing { height: 244px; background: var(--grey-bg); text-align: center; padding-top: 22px; }
  .outsourcing__title { font-size: 28px; font-weight: 700; color: var(--blue); letter-spacing: 1px; }
  .outsourcing__lead { font-size: 12px; color: var(--grey-text); margin-top: 2px; }
  .gallery { margin: 18px auto 0; width: 860px; display: flex; gap: 0; height: 104px; }
  .gallery__img { flex: 1; background: linear-gradient(160deg, #b9c2cc, #6f7d8c); }
  .gallery__img--feature { flex: 1.3; transform: translateY(-8px); height: 116px; background: linear-gradient(160deg, #cfd6de, #7d8a99); }
  .outsourcing__text { width: 720px; margin: 14px auto 0; font-size: 11px; line-height: 1.4; color: var(--grey-text); }
  .dots { margin-top: 8px; display: flex; justify-content: center; gap: 5px; }
  .dots span { width: 6px; height: 6px; border-radius: 50%; background: var(--blue); opacity: 0.4; }
  .dots span:first-child { opacity: 1; }
</style>
</head>
<body>
<div class="page">
  <header class="topbar">
    <div class="topbar__info">
      <span>Call us | 07 3000 4821</span>
      <span>Here To Help 24 x 7</span>
    </div>
    <div class="topbar__social" aria-label="Social links">
      <span class="social-dot social-dot--first"></span>
      <span class="social-dot"></span>
      <span class="social-dot"></span>
      <span class="social-dot"></span>
    </div>
  </header>

  <section class="hero">
    <div class="hero__photo" role="img" aria-label="Photo of a smiling businessman in a dark suit, hand at his chin"></div>
    <div class="hero__inner">
      <div class="brand"><span>Hire4ward</span><span class="brand__mark"></span></div>
      <nav class="nav">
        <span class="nav__item nav__item--active">HOME</span>
        <span class="nav__item">OUR STORY</span>
        <span class="nav__item">TIPS AND TRICK</span>
        <span class="nav__item">CONTACT US</span>
        <span class="nav__item">FAQ</span>
      </nav>
      <h1 class="headline"><span class="headline__accent">VIRTUAL</span> ASSISTANT</h1>
      <p class="subhead">MORE LIKE VALUABLE ASSET</p>
      <p class="tagline">Full-Time Virtual Assistant<br>Betrothed to Your Business</p>
      <div class="cta"><span class="cta__label">Call Us</span><span class="cta__number">07 3000 4821</span></div>
    </div>
  </section>

  <section class="outsourcing">
    <h2 class="outsourcing__title">OUTSOURCING</h2>
    <p class="outsourcing__lead">A Big Word That Means Big Things for Your Business</p>
    <div class="gallery">
      <div class="gallery__img" role="img" aria-label="Photo of business people meeting around a table"></div>
      <div class="gallery__img gallery__img--feature" role="img" aria-label="Photo of a team working together at a laptop"></div>
      <div class="gallery__img" role="img" aria-label="Photo of colleagues reviewing documents"></div>
      <div class="gallery__img" role="img" aria-label="Photo of a professional in an office"></div>
    </div>
    <p class="outsourcing__text">Virtual assistants handle the busywork of a modern office, from inbox and calendar to research and data entry, so your team can focus on growth at a fraction of the cost.</p>
    <div class="dots"><span></span><span></span><span></span></div>
  </section>
</div>
</body>
</html>
```